Larkfield Circuitry LLC is a Minneapolis / St Paul and surrounding communities computer repair and service company. It serves residential and small businesses. We work primarily with virus removal, data recovery, system baselines, networking, and new system installation. The site should look clean, professional, and easy to navigate.

This wordpress project must be coded and integrated into a wordpress theme for easy upload and maintenance.
Updates

Designers - Please make sure your design is in a wordpress theme so that It can be uploaded.  

Thank you,

Brin 

Target Market(s)

Residential and Small Business

Industry/Entity Type

Residential

Requirements
Must have
• Site Content
1. Main Page should have photos that scroll across, Business Description, Space to run
“Specials” Ads
a. Intuitive Navigation
2. Additional Pages
a. Blog for Computer Repair Articles
b. Testimonials Page
c. Contact Pages
d. Services Page with the ability to put in pricing
3. The site must be clean and professional.
4. Wordpress Theme

```html
<!DOCTYPE html>
<html lang="en">
<head>
<meta charset="utf-8">
<title>Larkfield Circuitry LLC – Computer Repair &amp; Service</title>
<link href="https://fonts.googleapis.com/css2?family=Arvo:wght@400;700&family=Open+Sans:ital,wght@0,400;0,600;0,700;1,400;1,600&family=Montserrat:wght@400;500&display=swap" rel="stylesheet">
<style>
  :root {
    --green: #4c9a1d;
    --green-dark: #3f8a14;
    --red: #e3191b;
    --ink: #333333;
    --body-text: #444444;
    --muted: #666666;
    --panel: #efefef;
    --panel-edge: #5d5d5d;
    --dark: #4a4a4a;
    --footer: #4d4d4d;
    --white: #ffffff;
    --slide-bg: #f4f4f4;
  }
  * { box-sizing: border-box; margin: 0; padding: 0; }
  html, body { width: 1173px; height: 1200px; overflow: hidden; background: var(--white); }
  body { font-family: "Open Sans", Arial, sans-serif; color: var(--body-text); position: relative; }

  /* Header */
  .site-header {
    position: absolute; left: 0; top: 0; width: 1173px; height: 115px;
    background: linear-gradient(#ffffff 0%, #ffffff 55%, #ececec 100%);
    border-bottom: 1px solid #dcdcdc;
  }
  .brand { position: absolute; left: 138px; top: 18px; display: flex; align-items: center; gap: 12px; }
  .brand-mark { width: 62px; height: 62px; border-radius: 50%; background: var(--green); }
  .brand-name { font-family: "Arvo", Georgia, serif; font-weight: 700; font-size: 30px; color: var(--dark); line-height: 1; }
  .contact { position: absolute; right: 137px; top: 16px; text-align: right; }
  .contact-phone { font-family: "Open Sans", Arial, sans-serif; font-weight: 700; font-size: 29px; color: var(--red); line-height: 1; display: flex; align-items: center; gap: 14px; justify-content: flex-end; }
  .contact-mail { font-size: 15px; color: var(--muted); font-weight: 600; margin-top: 4px; }
  .main-nav { position: absolute; right: 137px; top: 83px; display: flex; height: 31px; }
  .main-nav a {
    font-family: "Montserrat", Arial, sans-serif; font-size: 14px; font-weight: 500;
    color: #4a4a4a; text-decoration: none; padding: 0 13px; line-height: 31px; letter-spacing: .3px;
  }
  .main-nav a.is-current { background: var(--green); color: var(--white); }

  /* Slider */
  .hero {
    position: absolute; left: 0; top: 116px; width: 1173px; height: 410px;
    background: radial-gradient(ellipse at 50% 40%, #ffffff 0%, var(--slide-bg) 70%, #e9e9e9 100%);
    border-bottom: 1px solid #d8d8d8;
  }
  .hero-person { position: absolute; left: 210px; top: 36px; width: 230px; height: 254px; background: linear-gradient(#e7dcd4 0%, #6b6e75 45%, #3a3d44 100%); border-radius: 100px 100px 0 0; }
  .hero-product { position: absolute; left: 640px; top: 62px; width: 350px; height: 300px; background: linear-gradient(135deg, #c9cbcf 0%, #3a3c41 35%, #2a2c30 70%, #bfc2c6 100%); border-radius: 22px; }
  .hero-caption { position: absolute; left: 138px; font-family: "Arvo", Georgia, serif; font-size: 19.5px; color: var(--white); padding: 0 13px; height: 29px; line-height: 29px; }
  .hero-caption.line-one { top: 253px; background: #0d0d0d; }
  .hero-caption.line-two { top: 285px; background: var(--green); }
  .hero-dots { position: absolute; left: 910px; top: 373px; display: flex; gap: 7px; }
  .hero-dots span { width: 17px; height: 17px; border-radius: 50%; background: var(--white); border: 2px solid #d2d2d2; }
  .hero-dots span.is-active { background: var(--green); border-color: #cfe3c3; }

  /* Services */
  .service {
    position: absolute; top: 572px; width: 276px; height: 296px;
    background: var(--panel); border-bottom: 2px solid var(--panel-edge);
    padding: 16px 17px 0;
  }
  .service h2 { font-family: "Arvo", Georgia, serif; font-weight: 400; font-size: 17.5px; color: var(--green); white-space: nowrap; }
  .service h2 strong { font-weight: 700; }
  .service-photo { margin-top: 16px; width: 237px; height: 110px; border: 2px solid var(--white); }
  .service p { margin-top: 14px; font-size: 11.4px; line-height: 18.5px; color: var(--body-text); }
  .btn-more {
    display: block; width: 83px; margin: 11px auto 0; height: 20px; line-height: 20px; text-align: center;
    background: #5a5a5a; color: var(--white); font-size: 10.5px; font-style: italic; font-weight: 600;
    border-radius: 4px; text-decoration: none;
  }

  /* Welcome */
  .welcome {
    position: absolute; left: 137px; top: 915px; width: 590px; height: 202px;
    background: var(--panel); border-left: 5px solid var(--green); padding: 12px 20px 0 18px;
  }
  .welcome h1 { font-family: "Arvo", Georgia, serif; font-weight: 400; font-size: 23px; color: var(--green); }
  .welcome p { margin-top: 12px; font-size: 11.6px; line-height: 18.5px; color: var(--body-text); }
  .welcome p + p { margin-top: 18px; }
  .welcome .link-more { display: inline-block; margin-top: 20px; font-size: 10.5px; font-style: italic; color: var(--red); text-decoration: none; }

  .ad-slot {
    position: absolute; left: 761px; top: 915px; width: 274px; height: 201px;
    background: var(--dark); border: 1px solid #bdbdbd;
    display: flex; align-items: center; justify-content: center; text-align: center;
    font-size: 21px; font-style: italic; color: #bdbdbd; line-height: 26px;
  }

  /* Footer */
  .site-footer {
    position: absolute; left: 0; top: 1161px; width: 1173px; height: 39px; background: var(--footer);
    color: var(--white); font-size: 11.5px;
  }
  .footer-nav { position: absolute; left: 137px; top: 12px; }
  .footer-nav a { color: var(--white); text-decoration: none; }
  .copyright { position: absolute; right: 140px; top: 12px; font-size: 10.5px; }
</style>
</head>
<body>
  <header class="site-header">
    <div class="brand">
      <span class="brand-mark"></span>
      <span class="brand-name">Larkfield Circuitry LLC</span>
    </div>
    <div class="contact">
      <div class="contact-phone">
        <svg width="30" height="30" viewBox="0 0 30 30" aria-hidden="true">
          <rect x="3" y="7" width="24" height="16" rx="2" fill="#3aa0e0"/>
          <path d="M3 8 L15 17 L27 8" stroke="#ffffff" stroke-width="2" fill="none"/>
          <path d="M10 23 L8 29 L15 23 Z" fill="#f0a21a"/>
        </svg>
        555 014 2290
      </div>
      <div class="contact-mail">info@larkfieldcircuitry.com</div>
    </div>
    <nav class="main-nav">
      <a href="#" class="is-current">HOME</a>
      <a href="#">ABOUT US</a>
      <a href="#">SERVICES</a>
      <a href="#">BLOG</a>
      <a href="#">TESTIMONIALS</a>
      <a href="#">CONTACT</a>
    </nav>
  </header>

  <section class="hero">
    <div class="hero-person" role="img" aria-label="Photo of a smiling technician in a suit and tie"></div>
    <div class="hero-product" role="img" aria-label="Photo of a desktop computer tower with a wrench and screwdriver crossed in front"></div>
    <div class="hero-caption line-one">There are many variation of passage</div>
    <div class="hero-caption line-two">Standard dummy text ever since the 1500s</div>
    <div class="hero-dots"><span class="is-active"></span><span></span><span></span><span></span><span></span></div>
  </section>

  <article class="service" style="left:137px">
    <h2>Computer <strong>Repair &amp; Service</strong></h2>
    <div class="service-photo" role="img" aria-label="Photo of a technician repairing an open computer" style="background:linear-gradient(90deg,#b88a5a 0%,#7d6a55 45%,#3b3f46 100%)"></div>
    <p>Lorem Ipsum is simply dummy text of into the printing and typesetting industry, lorem Ipsum has been the industry's since the took a galley of type.</p>
    <a href="#" class="btn-more">Read More →</a>
  </article>

  <article class="service" style="left:449px">
    <h2>Computer <strong>Virus Removal</strong></h2>
    <div class="service-photo" role="img" aria-label="Photo of a laptop showing a virus alert warning" style="background:linear-gradient(135deg,#1f2a30 0%,#55616a 50%,#b9c0c4 75%,#2b3338 100%)"></div>
    <p>Lorem Ipsum is simply dummy text of into the printing and typesetting industry, lorem Ipsum has been the industry's since the took a galley of type.</p>
    <a href="#" class="btn-more">Read More →</a>
  </article>

  <article class="service" style="left:761px">
    <h2><strong>System Installation</strong></h2>
    <div class="service-photo" role="img" aria-label="Photo of a technician installing equipment into a server rack" style="background:linear-gradient(90deg,#2a2c30 0%,#4a4e55 50%,#1d1f23 100%)"></div>
    <p>Lorem Ipsum is simply dummy text of into the printing and typesetting industry, lorem Ipsum has been the industry's since the took a galley of type.</p>
    <a href="#" class="btn-more">Read More →</a>
  </article>

  <section class="welcome">
    <h1>Welcome to Larkfield Circuitry</h1>
    <p>Larkfield Circuitry LLC is a Minneapolis / St Paul and surrounding communities computer repair and service company. It serves residential and small businesses.</p>
    <p>We work primarily with virus removal, data recovery, system baselines, networking, and new system installation. The site should look clean, professional, and easy to navigate.</p>
    <a href="#" class="link-more">Read More...</a>
  </section>

  <aside class="ad-slot">ADVERTISEMENT<br>BANNER</aside>

  <footer class="site-footer">
    <nav class="footer-nav">
      <a href="#">Home</a> | <a href="#">About us</a> | <a href="#">Services</a> | <a href="#">Blog</a> | <a href="#">Testimonials</a> | <a href="#">Contact</a>
    </nav>
    <div class="copyright">Copyright © 2012 Larkfield Circuitry. All Rights Reserved.</div>
  </footer>
</body>
</html>
```